Banners - Various shapes and sizes

I need a banner set for an event planning company, www.coralvowsandparties.example

This will be for their Brightlane Promo campaign, the banners can all look very similar but the final project is for a set of them, delivered as 1 PSD, in these shapes/sizes:

Mobile leaderboard: 320 x 50
Banner: 468 x 60
Leaderboard: 728 x 90
Square: 250 x 250
Small square: 200 x 200
Large rectangle: 336 x 280
Inline rectangle: 300 x 250
Skyscraper: 120 x 600
Wide skyscraper: 160 x 600
Half-page: 300 x 600
Large leaderboard: 970x90

At a minimum, they should include:

- The Lantern Hall Events logo
- Color scheme from their website
- Phone # and call to action

Looking over their site can provide some information on the venues, wedding packages, and awards received to get an idea of who Lantern Hall Events is.
Updates

Target Market(s)

Newly engaged brides

Industry/Entity Type

Event Planning

Requirements
Must have
• At a minimum, they should include:

- The Lantern Hall Events logo (I have attached it here)

```html
<!DOCTYPE html>
<html lang="en">
<head>
<meta charset="utf-8">
<title>Lantern Hall Events – Banner Set</title>
<link href="https://fonts.googleapis.com/css2?family=Crimson+Text:wght@400&family=Questrial&display=swap" rel="stylesheet">
<style>
  :root{
    --canvas:#ffffff;
    --blush:#f6d7d3;
    --magenta:#c63c93;
    --magenta-soft:#d463a8;
    --ink:#595557;
    --white:#ffffff;
    --serif:"Crimson Text", Georgia, serif;
    --sans:"Questrial", Arial, sans-serif;
  }
  *{box-sizing:border-box;margin:0;padding:0}
  html,body{width:1200px;height:900px;overflow:hidden;background:var(--canvas)}
  .canvas{position:relative;width:1200px;height:900px}

  .banner{position:absolute;background:var(--blush);overflow:hidden;color:var(--ink)}
  .banner > p,.banner > .cta{position:absolute;z-index:2;white-space:nowrap}
  .center{left:0;width:100%;text-align:center}
  .right{text-align:right}

  .brand{font-family:var(--serif);color:var(--magenta);font-weight:400;line-height:1.05}
  .services{font-family:var(--serif);color:var(--ink);text-transform:uppercase;line-height:1.15;letter-spacing:-.02em}
  .call,.follow{font-family:var(--sans);color:var(--ink);line-height:1.3}
  .cta{display:block;background:var(--magenta);color:var(--white);font-family:var(--sans);text-transform:uppercase;border-radius:4px;text-align:center;line-height:1}
  .center.cta{left:50%;transform:translateX(-50%)}

  .bubbles{position:absolute;z-index:1;background:radial-gradient(ellipse at center,var(--magenta-soft) 0%,rgba(214,99,168,.45) 55%,rgba(246,215,211,0) 75%)}
  .glasses{position:absolute;z-index:1;background:linear-gradient(180deg,var(--magenta-soft),var(--magenta));border-radius:40% 40% 12% 12%}

  /* Half-page, large */
  .half-xl{left:60px;top:0;width:240px;height:900px}
  .half-xl .bubbles{left:55px;top:-10px;width:140px;height:90px}
  .half-xl .brand{top:112px;font-size:40px}
  .half-xl .services{top:236px;font-size:21px;line-height:1.3}
  .half-xl .call{top:352px;font-size:26px}
  .half-xl .cta{top:458px;width:196px;padding:11px 0;font-size:24px;border-radius:6px}
  .half-xl .follow{top:518px;font-size:24px;line-height:1.3}
  .half-xl .glasses{left:6px;top:628px;width:224px;height:255px}

  /* Half-page */
  .half{left:352px;top:52px;width:223px;height:444px}
  .half .bubbles{left:20px;top:0;width:170px;height:55px}
  .half .brand{left:14px;top:74px;font-size:22px}
  .half .services{top:122px;font-size:16px}
  .half .call{left:30px;top:184px;font-size:14px}
  .half .cta{left:28px;top:211px;width:115px;padding:6px 0;font-size:13px}
  .half .follow{left:30px;top:244px;font-size:14px}
  .half .glasses{left:100px;top:240px;width:118px;height:196px}

  /* Inline rectangle */
  .inline{left:587px;top:28px;width:249px;height:208px}
  .inline .bubbles{left:200px;top:0;width:50px;height:90px}
  .inline .brand{left:14px;top:16px;font-size:22px}
  .inline .services{left:0;width:236px;text-align:center;top:50px;font-size:13px}
  .inline .glasses{left:10px;top:96px;width:72px;height:108px}
  .inline .call{left:88px;top:104px;font-size:13px}
  .inline .cta{left:120px;top:126px;width:108px;padding:6px 0;font-size:13px}
  .inline .follow{right:20px;top:158px;font-size:13px}

  /* Skyscraper */
  .sky{left:589px;top:253px;width:89px;height:443px}
  .sky .bubbles{left:4px;top:0;width:82px;height:56px}
  .sky .brand{top:64px;font-size:15px}
  .sky .services{top:110px;font-size:9px}
  .sky .call{top:166px;font-size:12px}
  .sky .cta{top:236px;width:80px;padding:4px 0;font-size:9px}
  .sky .follow{top:264px;font-size:11px}
  .sky .glasses{left:4px;top:325px;width:80px;height:112px}

  /* Wide skyscraper */
  .wsky{left:690px;top:253px;width:119px;height:443px}
  .wsky .bubbles{left:10px;top:0;width:100px;height:50px}
  .wsky .brand{top:56px;font-size:20px}
  .wsky .services{top:110px;font-size:11.5px}
  .wsky .call{top:172px;font-size:13px}
  .wsky .cta{top:232px;width:98px;padding:5px 0;font-size:12px}
  .wsky .follow{top:264px;font-size:13px}
  .wsky .glasses{left:10px;top:322px;width:100px;height:116px}

  /* Small square */
  .small{left:822px;top:248px;width:148px;height:148px}
  .small .bubbles{left:118px;top:0;width:30px;height:30px}
  .small .brand{left:6px;top:12px;font-size:14px}
  .small .services{top:34px;font-size:8px}
  .small .call{left:30px;top:68px;font-size:9px}
  .small .cta{left:57px;top:86px;width:78px;padding:4px 0;font-size:8.5px}
  .small .follow{right:12px;top:108px;font-size:9px}
  .small .glasses{left:6px;top:86px;width:44px;height:58px}

  /* Square */
  .square{left:822px;top:406px;width:184px;height:185px}
  .square .bubbles{left:150px;top:0;width:34px;height:40px}
  .square .brand{left:8px;top:18px;font-size:18px}
  .square .services{top:48px;font-size:11px}
  .square .call{left:38px;top:90px;font-size:11.5px}
  .square .cta{left:72px;top:111px;width:98px;padding:5px 0;font-size:11.5px}
  .square .follow{right:14px;top:138px;font-size:11.5px}
  .square .glasses{left:8px;top:114px;width:56px;height:66px}

  /* Large rectangle */
  .large{left:352px;top:511px;width:223px;height:184px}
  .large .bubbles{left:180px;top:0;width:44px;height:40px}
  .large .brand{left:10px;top:16px;font-size:19px}
  .large .services{top:48px;font-size:9.5px;letter-spacing:-.03em}
  .large .glasses{left:6px;top:84px;width:56px;height:98px}
  .large .call{left:66px;top:78px;font-size:12.5px}
  .large .cta{left:102px;top:101px;width:106px;padding:6px 0;font-size:12.5px}
  .large .follow{right:12px;top:134px;font-size:12.5px}

  /* Mobile leaderboard */
  .mobile{left:822px;top:604px;width:236px;height:36px}
  .mobile .bubbles.l{left:-6px;top:0;width:24px;height:36px}
  .mobile .bubbles.r{left:218px;top:4px;width:20px;height:30px}
  .mobile .brand{left:18px;top:3px;font-size:11px}
  .mobile .services{left:8px;top:23px;font-size:6px}
  .mobile .call{left:146px;top:6px;font-size:7px}
  .mobile .cta{left:164px;top:20px;width:54px;padding:2px 0;font-size:6.5px}

  /* Banner */
  .banner468{left:822px;top:652px;width:346px;height:43px}
  .banner468 .bubbles.l{left:-8px;top:0;width:40px;height:43px}
  .banner468 .bubbles.r{left:314px;top:6px;width:32px;height:37px}
  .banner468 .brand{left:42px;top:2px;font-size:16px}
  .banner468 .services{left:12px;top:28px;font-size:8px}
  .banner468 .call{left:218px;top:5px;font-size:10px}
  .banner468 .cta{left:232px;top:21px;width:74px;padding:3px 0;font-size:9.5px}

  /* Large leaderboard */
  .board970{left:352px;top:714px;width:718px;height:65px}
  .board970 .bubbles.l{left:-10px;top:0;width:70px;height:65px}
  .board970 .bubbles.r{left:660px;top:0;width:60px;height:65px}
  .board970 .brand{left:100px;top:4px;font-size:28px}
  .board970 .services{left:88px;top:42px;font-size:12.5px}
  .board970 .glasses{left:414px;top:8px;width:50px;height:57px}
  .board970 .call{left:482px;top:8px;font-size:15px}
  .board970 .cta{left:500px;top:32px;width:112px;padding:6px 0;font-size:14px}

  /* Leaderboard */
  .board728{left:352px;top:796px;width:540px;height:67px}
  .board728 .bubbles.l{left:-8px;top:0;width:62px;height:67px}
  .board728 .bubbles.r{left:500px;top:4px;width:42px;height:63px}
  .board728 .brand{left:74px;top:6px;font-size:24px}
  .board728 .services{left:44px;top:43px;font-size:11px}
  .board728 .glasses{left:318px;top:10px;width:46px;height:57px}
  .board728 .call{left:370px;top:12px;font-size:12px}
  .board728 .cta{left:382px;top:33px;width:94px;padding:5px 0;font-size:11.5px}
</style>
</head>
<body>
<main class="canvas">

  <section class="banner half-xl" aria-label="Half-page banner, large">
    <div class="bubbles" role="img" aria-label="Cluster of pink champagne bubbles"></div>
    <p class="brand center">Lantern Hall<br>Events</p>
    <p class="services center">Weddings,<br>Quinces, and<br>Corporate Events</p>
    <p class="call center">Call<br>305-555-0148<br>or</p>
    <span class="cta center">Click Here</span>
    <p class="follow center">to start<br>planning<br>your event!</p>
    <div class="glasses" role="img" aria-label="Two pink champagne flutes clinking with bubbles"></div>
  </section>

  <section class="banner half" aria-label="Half-page banner">
    <div class="bubbles" role="img" aria-label="Cluster of pink champagne bubbles"></div>
    <p class="brand">Lantern Hall Events</p>
    <p class="services center">Weddings, Quinces,<br>and Corporate Events</p>
    <p class="call">Call 305-555-0148 or</p>
    <span class="cta">Click Here</span>
    <p class="follow">to start<br>planning<br>your<br>event!</p>
    <div class="glasses" role="img" aria-label="Two pink champagne flutes clinking with bubbles"></div>
  </section>

  <section class="banner inline" aria-label="Inline rectangle banner">
    <div class="bubbles" role="img" aria-label="Cluster of pink champagne bubbles"></div>
    <p class="brand">Lantern Hall Events</p>
    <p class="services">Weddings, Quinces,<br>and Corporate Events</p>
    <div class="glasses" role="img" aria-label="Two pink champagne flutes clinking with bubbles"></div>
    <p class="call">Call 305-555-0148 or</p>
    <span class="cta">Click Here</span>
    <p class="follow right">to start planning<br>your event!</p>
  </section>

  <section class="banner sky" aria-label="Skyscraper banner">
    <div class="bubbles" role="img" aria-label="Cluster of pink champagne bubbles"></div>
    <p class="brand center">Lantern Hall<br>Events</p>
    <p class="services center">Weddings,<br>Quinces, and<br>Corporate Events</p>
    <p class="call center">Call<br>305-555-<br>0148 or</p>
    <span class="cta center">Click Here</span>
    <p class="follow center">to start<br>planning<br>your event!</p>
    <div class="glasses" role="img" aria-label="Two pink champagne flutes clinking with bubbles"></div>
  </section>

  <section class="banner wsky" aria-label="Wide skyscraper banner">
    <div class="bubbles" role="img" aria-label="Cluster of pink champagne bubbles"></div>
    <p class="brand center">Lantern Hall<br>Events</p>
    <p class="services center">Weddings,<br>Quinces, and<br>Corporate Events</p>
    <p class="call center">Call<br>305-555-0148<br>or</p>
    <span class="cta center">Click Here</span>
    <p class="follow center">to start<br>planning<br>your event!</p>
    <div class="glasses" role="img" aria-label="Two pink champagne flutes clinking with bubbles"></div>
  </section>

  <section class="banner small" aria-label="Small square banner">
    <div class="bubbles" role="img" aria-label="Cluster of pink champagne bubbles"></div>
    <p class="brand">Lantern Hall Events</p>
    <p class="services center">Weddings, Quinces,<br>and Corporate Events</p>
    <p class="call">Call 305-555-0148 or</p>
    <span class="cta">Click Here</span>
    <p class="follow right">to start planning<br>your event!</p>
    <div class="glasses" role="img" aria-label="Two pink champagne flutes clinking with bubbles"></div>
  </section>

  <section class="banner square" aria-label="Square banner">
    <div class="bubbles" role="img" aria-label="Cluster of pink champagne bubbles"></div>
    <p class="brand">Lantern Hall Events</p>
    <p class="services center">Weddings, Quinces,<br>and Corporate Events</p>
    <p class="call">Call 305-555-0148 or</p>
    <span class="cta">Click Here</span>
    <p class="follow right">to start planning<br>your event!</p>
    <div class="glasses" role="img" aria-label="Two pink champagne flutes clinking with bubbles"></div>
  </section>

  <section class="banner large" aria-label="Large rectangle banner">
    <div class="bubbles" role="img" aria-label="Cluster of pink champagne bubbles"></div>
    <p class="brand">Lantern Hall Events</p>
    <p class="services center">Weddings, Quinces, and Corporate Events</p>
    <div class="glasses" role="img" aria-label="Two pink champagne flutes clinking with bubbles"></div>
    <p class="call">Call 305-555-0148 or</p>
    <span class="cta">Click Here</span>
    <p class="follow right">to start planning<br>your event!</p>
  </section>

  <section class="banner mobile" aria-label="Mobile leaderboard banner">
    <div class="bubbles l" role="img" aria-label="Pink champagne bubbles"></div>
    <p class="brand">Lantern Hall Events</p>
    <p class="services">Weddings, Quinces, and Corporate Events</p>
    <p class="call">Call 305-555-0148 or</p>
    <span class="cta">Click Here</span>
    <div class="bubbles r" role="img" aria-label="Pink champagne bubbles"></div>
  </section>

  <section class="banner banner468" aria-label="Banner 468 by 60">
    <div class="bubbles l" role="img" aria-label="Pink champagne bubbles"></div>
    <p class="brand">Lantern Hall Events</p>
    <p class="services">Weddings, Quinces, and Corporate Events</p>
    <p class="call">Call 305-555-0148 or</p>
    <span class="cta">Click Here</span>
    <div class="bubbles r" role="img" aria-label="Pink champagne bubbles"></div>
  </section>

  <section class="banner board970" aria-label="Large leaderboard banner">
    <div class="bubbles l" role="img" aria-label="Pink champagne bubbles"></div>
    <p class="brand">Lantern Hall Events</p>
    <p class="services">Weddings, Quinces, and Corporate Events</p>
    <div class="glasses" role="img" aria-label="Two pink champagne flutes clinking with bubbles"></div>
    <p class="call">Call 305-555-0148 or</p>
    <span class="cta">Click Here</span>
    <div class="bubbles r" role="img" aria-label="Pink champagne bubbles"></div>
  </section>

  <section class="banner board728" aria-label="Leaderboard banner">
    <div class="bubbles l" role="img" aria-label="Pink champagne bubbles"></div>
    <p class="brand">Lantern Hall Events</p>
    <p class="services">Weddings, Quinces, and Corporate Events</p>
    <div class="glasses" role="img" aria-label="Two pink champagne flutes clinking with bubbles"></div>
    <p class="call">Call 305-555-0148 or</p>
    <span class="cta">Click Here</span>
    <div class="bubbles r" role="img" aria-label="Pink champagne bubbles"></div>
  </section>

</main>
</body>
</html>
```